Beauty Packaging Design for small bottle

Design label to have a similar look and feel as other products (as attached for reference). This will be a printed on a gold metallic label, so although the design should be in gold to show us how it will eventually look, the final file will need to have the gold areas in red.

All project information is outline in the attached brief. Please contact us for any questions along the way.

Target Market(s)

Educated, savvy women 30-65 yrs old.

Industry/Entity Type

Hair And Beauty

Font styles to use
Other font styles liked:
• See brief

Requirements
Must have
• See brief
• Color(s): black, gold, white
Nice to have
• purple (CMYK 33/55/0/51)
Should not have
• See brief

```html
<!DOCTYPE html>
<html lang="en">
<head>
<meta charset="UTF-8">
<title>Retinol Nova – Intensive Overnight Moisturizer Label</title>
<link rel="stylesheet" href="https://fonts.googleapis.com/css2?family=Cinzel:wght@700&family=Parisienne&family=Pathway+Gothic+One&family=PT+Sans+Narrow:wght@700&family=Dancing+Script:wght@600&family=Josefin+Sans:wght@400&display=swap">
<style>
  :root {
    --backdrop: #f1f1f1;
    --label-black: #0b0b0b;
    --gold: #c9962e;
    --gold-light: #e8b548;
    --gold-deep: #8a5e14;
    --ink-white: #f6f3ee;
  }
  * { margin: 0; padding: 0; box-sizing: border-box; }
  html, body { width: 1200px; height: 1200px; overflow: hidden; }
  body { background: var(--backdrop); position: relative; }

  .label {
    position: absolute;
    left: 200px; top: 98px;
    width: 800px; height: 1005px;
    background: var(--label-black);
    color: var(--ink-white);
  }

  .brand {
    position: absolute;
    top: 100px; left: 0; right: 0;
    display: flex; justify-content: center; align-items: center; gap: 18px;
  }
  .brand-dot {
    width: 46px; height: 46px;
    border-radius: 50%;
    border: 4px solid var(--ink-white);
  }
  .brand-name {
    font-family: "Josefin Sans", sans-serif;
    font-weight: 400;
    font-size: 62px;
    letter-spacing: 6px;
    line-height: 1;
    padding-top: 8px;
    color: var(--ink-white);
  }

  .ornament {
    position: absolute;
    left: 158px; top: 214px;
    width: 484px; height: 484px;
    border-radius: 50%;
    background: radial-gradient(circle, rgba(232,181,72,0.55) 0%, rgba(201,150,46,0.45) 45%, rgba(138,94,20,0.25) 70%, rgba(11,11,11,0) 74%);
  }

  .product-name {
    position: absolute;
    top: 355px; left: 0; right: 0;
    text-align: center;
    font-family: "Cinzel", serif;
    font-weight: 700;
    font-size: 104px;
    line-height: 1;
    color: var(--ink-white);
    text-shadow: 0 2px 6px rgba(0,0,0,0.6);
  }
  .product-sub {
    position: absolute;
    top: 470px; left: 300px;
    font-family: "Parisienne", cursive;
    font-size: 130px;
    line-height: 1;
    color: var(--ink-white);
    text-shadow: 0 2px 6px rgba(0,0,0,0.6);
  }

  .descriptor {
    position: absolute;
    top: 732px; left: 0; right: 0;
    text-align: center;
    font-family: "Pathway Gothic One", sans-serif;
    font-size: 40px;
    line-height: 1;
    color: var(--ink-white);
  }

  .ingredients {
    position: absolute;
    top: 806px; left: 50px;
    width: 700px; height: 80px;
    border: 2px solid var(--gold);
    display: grid;
    grid-template-columns: 1.25fr 1fr 0.95fr 0.95fr;
  }
  .ingredient-cell {
    display: flex; flex-direction: column; justify-content: center; align-items: center;
    font-family: "PT Sans Narrow", sans-serif;
    font-weight: 700;
    font-size: 21px;
    line-height: 1.3;
    color: var(--ink-white);
    text-align: center;
    margin: 8px 0;
  }
  .ingredient-cell + .ingredient-cell { border-left: 2px solid var(--gold); }

  .volume {
    position: absolute;
    top: 925px; left: 0; right: 0;
    text-align: center;
    font-family: "Dancing Script", cursive;
    font-weight: 600;
    font-style: italic;
    font-size: 44px;
    line-height: 1;
    color: var(--ink-white);
  }
</style>
</head>
<body>
  <main class="label">
    <div class="brand">
      <span class="brand-dot"></span>
      <span class="brand-name">LUMERE</span>
    </div>

    <div class="ornament" role="img" aria-label="Gold metallic mandala-style ornamental pattern behind the product name"></div>

    <h1 class="product-name">RETINOL</h1>
    <div class="product-sub">nova</div>

    <p class="descriptor">Intensive Overnight Moisturizer</p>

    <div class="ingredients">
      <div class="ingredient-cell"><span>RETINOL 2.5% PLUS</span><span>HYALURONIC ACID</span></div>
      <div class="ingredient-cell"><span>ALOE VERA</span><span>SUNFLOWER OIL</span></div>
      <div class="ingredient-cell"><span>JOJOBA OIL</span><span>VITAMIN E</span></div>
      <div class="ingredient-cell"><span>SHEA BUTTER</span><span>GREEN TEA</span></div>
    </div>

    <p class="volume">2 fl. oz./60 ml</p>
  </main>
</body>
</html>
```